Law Offices business card

Hi there, I'll need business card for the Law Offices of Tobin Haskell. The information must convey his strategic approach and quick resolution to complex business litigation needs. Please emphasize Civil Litigation, Corporate Law, Business Governance and Real Estate Law. Tobin has over 25 years of experience in these fields.The card should be modern and edgy and the message should be clear. Please consult his current website for ideas.

Business

```html
<!DOCTYPE html>
<html lang="en">
<head>
<meta charset="utf-8">
<title>Law Offices of Tobin Haskell – Business Card</title>
<link rel="stylesheet" href="https://fonts.googleapis.com/css2?family=Open+Sans:wght@400;600&family=Tinos&display=swap">
<style>
  :root {
    --bg: #d9d6d1;
    --orange: #f66000;
    --orange-soft: #f87a2a;
    --paper: #ececec;
    --ink: #3a3a3a;
    --grey: #5a5a5a;
    --white: #ffffff;
  }
  * { box-sizing: border-box; margin: 0; padding: 0; }
  html, body { width: 1200px; height: 900px; overflow: hidden; }
  body { background: var(--bg); position: relative; font-family: "Open Sans", Arial, sans-serif; }

  .card {
    position: absolute;
    width: 620px;
    height: 354px;
    overflow: hidden;
    box-shadow: 0 10px 28px rgba(0,0,0,.25);
  }
  .card--front { left: 70px; top: 100px; background: var(--orange); color: var(--white); }
  .card--back { left: 510px; top: 430px; background: var(--paper); color: var(--ink); }

  .ghost-ring { position: absolute; }
  .card--front .ghost-ring { left: 40px; top: 150px; width: 300px; height: 300px; }
  .card--back .ghost-ring { left: 10px; top: 150px; width: 340px; height: 340px; }

  .brand { position: absolute; left: 42px; top: 48px; display: flex; align-items: center; }
  .brand__mark { width: 76px; height: 76px; flex: none; }
  .brand__rule { width: 1px; height: 66px; margin: 0 20px 0 18px; }
  .card--front .brand__rule { background: rgba(255,255,255,.55); }
  .card--back .brand__rule { background: #b9b9b9; }
  .brand__name { font-family: "Tinos", "Times New Roman", serif; font-weight: 400; line-height: 1; text-transform: uppercase; }
  .brand__line1 { display: block; font-size: 30px; letter-spacing: .5px; }
  .brand__line2 { display: block; font-size: 15.5px; letter-spacing: 1.2px; margin-top: 3px; }
  .card--back .brand__line1 { color: var(--orange); }
  .card--back .brand__line2 { color: var(--grey); }

  .services { position: absolute; left: 352px; top: 146px; list-style: none; font-weight: 600; font-size: 15.5px; line-height: 1.5; }
  .services li { position: relative; padding-left: 18px; }
  .services li::before { content: ""; position: absolute; left: 0; top: 9px; width: 7px; height: 7px; border-radius: 50%; background: var(--white); }
  .experience { position: absolute; left: 370px; top: 272px; font-size: 13px; font-weight: 400; letter-spacing: .3px; }

  .contact { position: absolute; left: 380px; top: 120px; font-size: 14px; color: var(--ink); }
  .contact__name { color: var(--orange); font-weight: 600; font-size: 18px; line-height: 1.1; }
  .contact__role { font-size: 13px; margin-bottom: 16px; }
  .contact__address { font-style: normal; line-height: 1.35; margin-bottom: 14px; }
  .contact__list { list-style: none; line-height: 1.55; }
  .contact__list li { display: flex; align-items: center; gap: 8px; }
  .contact__list svg { width: 12px; height: 12px; flex: none; fill: var(--orange); }
</style>
</head>
<body>

<section class="card card--front" aria-label="Card front">
  <svg class="ghost-ring" viewBox="0 0 100 100" aria-hidden="true">
    <circle cx="50" cy="50" r="46" fill="none" stroke="var(--orange-soft)" stroke-width="5"/>
  </svg>
  <div class="brand">
    <svg class="brand__mark" viewBox="0 0 76 76" aria-hidden="true">
      <circle cx="38" cy="38" r="34" fill="none" stroke="var(--white)" stroke-width="5"/>
    </svg>
    <span class="brand__rule"></span>
    <h1 class="brand__name">
      <span class="brand__line1">Law Offices</span>
      <span class="brand__line2">of Tobin Haskell</span>
    </h1>
  </div>
  <ul class="services">
    <li>Civil Litigation</li>
    <li>Corporate Law</li>
    <li>Business Governance</li>
    <li>Real Estate Law</li>
  </ul>
  <p class="experience">Over 25 years of experience</p>
</section>

<section class="card card--back" aria-label="Card back">
  <svg class="ghost-ring" viewBox="0 0 100 100" aria-hidden="true">
    <circle cx="50" cy="50" r="46" fill="none" stroke="var(--white)" stroke-width="5"/>
  </svg>
  <div class="brand">
    <svg class="brand__mark" viewBox="0 0 76 76" aria-hidden="true">
      <circle cx="38" cy="38" r="34" fill="var(--orange)" stroke="var(--ink)" stroke-width="4"/>
    </svg>
    <span class="brand__rule"></span>
    <h2 class="brand__name">
      <span class="brand__line1">Law Offices</span>
      <span class="brand__line2">of Tobin Haskell</span>
    </h2>
  </div>
  <div class="contact">
    <p class="contact__name">Tobin Haskell</p>
    <p class="contact__role">Attorney</p>
    <address class="contact__address">118B Harbor Lane<br>Coral Shores, Florida 33410</address>
    <ul class="contact__list">
      <li><svg viewBox="0 0 12 12" aria-hidden="true"><path d="M2.4 0.8l2 2.2-1 1.3c.7 1.5 1.8 2.6 3.3 3.3l1.3-1 2.2 2-1.2 2.1C5.4 10.5 1.5 6.6 1.3 2z"/></svg>561-555-0142</li>
      <li><svg viewBox="0 0 12 12" aria-hidden="true"><rect x="1" y="4" width="10" height="7" rx="1"/><rect x="3" y="1" width="6" height="3"/></svg>561-555-0187</li>
      <li><svg viewBox="0 0 12 12" aria-hidden="true"><path d="M1 3h10v7H1z M1 3l5 4 5-4" stroke="var(--paper)" stroke-width=".8"/></svg>tobin@haskelllaw.com</li>
      <li><svg viewBox="0 0 12 12" aria-hidden="true"><circle cx="6" cy="6" r="5"/></svg>www.haskelllaw.com</li>
    </ul>
  </div>
</section>

</body>
</html>
```